Real Estate Investing company needs a business card design

We need a business card design for new Real Estate Investment Company called "Maple Ridge Ventures, LLC." We buy homes for cash and close quickly in any situation. Our company provides an easy and fast option for home owners who are in tough situations who need to sell their home fast and don't want realtor fees or other listing hassles. We also renovate and resell our homes which helps provide housing for the community. We would like to see designs that use the colors blue and white to match our company logo or other colors that may match our company logo. The final design should communicate trust and easy process.
Industry/Entity Type
Business
Contact Information for Business Card
Front should have company name and company logo. back of card should have company logo and area to list services.
Look and feel

```html
<!DOCTYPE html>
<html lang="en">
<head>
<meta charset="utf-8">
<title>Maple Ridge Ventures — Business Card</title>
<link rel="stylesheet" href="https://fonts.googleapis.com/css2?family=Open+Sans:wght@400;600;700&display=swap">
<style>
  :root {
    --page-bg: #3a3c3f;
    --card-bg: #1f2327;
    --brand-blue: #1a74c4;
    --ink-white: #f2f4f6;
    --rule-grey: #8a8f95;
  }
  * { box-sizing: border-box; margin: 0; padding: 0; }
  html, body { width: 1200px; height: 1189px; overflow: hidden; }
  body {
    background: var(--page-bg);
    font-family: "Open Sans", Verdana, sans-serif;
    position: relative;
  }
  .card {
    position: absolute;
    left: 170px;
    width: 860px;
    height: 491px;
    background: var(--card-bg);
    border-radius: 24px;
    overflow: hidden;
  }
  .card--services { top: 70px; }
  .card--contact { top: 620px; }

  .brand {
    position: absolute;
    display: flex;
    align-items: center;
    gap: 16px;
  }
  .brand__mark {
    width: 22px; height: 22px;
    background: var(--brand-blue);
    flex: none;
  }
  .brand__name {
    color: var(--brand-blue);
    font-weight: 700;
    font-size: 44px;
    line-height: 1.05;
    text-transform: uppercase;
    letter-spacing: 1px;
  }
  .card--services .brand { left: 60px; top: 120px; }
  .card--contact .brand { left: 60px; top: 190px; }

  .growth-line { position: absolute; inset: 0; }

  .services {
    position: absolute;
    right: 50px;
    top: 48px;
    text-align: right;
  }
  .services__title {
    color: var(--brand-blue);
    font-size: 26px;
    font-weight: 400;
    letter-spacing: 1px;
    margin-bottom: 8px;
    padding-right: 30px;
  }
  .services__list { list-style: none; }
  .services__item {
    color: var(--ink-white);
    font-size: 19px;
    line-height: 34px;
    display: flex;
    justify-content: flex-end;
    align-items: center;
    gap: 14px;
  }
  .services__item::after {
    content: "";
    width: 14px; height: 14px;
    background: var(--brand-blue);
  }

  .divider {
    position: absolute;
    left: 455px; top: 110px;
    width: 1.5px; height: 290px;
    background: var(--rule-grey);
  }
  .contact {
    position: absolute;
    left: 490px; top: 105px;
    width: 340px;
  }
  .contact__name {
    color: var(--brand-blue);
    font-weight: 700;
    font-size: 28px;
    letter-spacing: 1px;
    line-height: 1;
  }
  .contact__role {
    color: var(--ink-white);
    font-weight: 600;
    font-size: 20px;
    margin-bottom: 22px;
  }
  .contact__address {
    color: var(--brand-blue);
    font-size: 20px;
    line-height: 27px;
    font-style: normal;
    margin-bottom: 6px;
  }
  .contact__line {
    display: flex;
    align-items: center;
    gap: 12px;
    color: var(--brand-blue);
    font-size: 20px;
    line-height: 30px;
  }
  .contact__icon {
    width: 24px; height: 24px;
    background: var(--ink-white);
    border-radius: 4px;
    flex: none;
  }
  .contact__web {
    color: var(--ink-white);
    font-size: 20px;
    margin-top: 18px;
    letter-spacing: 0.5px;
  }
</style>
</head>
<body>

<section class="card card--services" aria-label="Card back with services">
  <div class="brand">
    <span class="brand__mark"></span>
    <span class="brand__name">Maple Ridge<br>Ventures</span>
  </div>

  <svg class="growth-line" viewBox="0 0 860 491" aria-hidden="true">
    <polyline points="120,500 235,365 400,335 770,300" fill="none" stroke="#1a74c4" stroke-width="22" stroke-linejoin="miter"/>
    <polygon points="760,272 820,298 764,330" fill="#1a74c4"/>
  </svg>

  <div class="services">
    <h2 class="services__title">SERVICES</h2>
    <ul class="services__list">
      <li class="services__item">Cash offers on any home</li>
      <li class="services__item">Close in as little as 7 days</li>
      <li class="services__item">No fees &amp; no commissions</li>
      <li class="services__item">Fix &amp; resell local homes</li>
      <li class="services__item">Sell as-is in any condition</li>
    </ul>
  </div>
</section>

<section class="card card--contact" aria-label="Card front with contact details">
  <div class="brand">
    <span class="brand__mark"></span>
    <span class="brand__name">Maple Ridge<br>Ventures</span>
  </div>

  <div class="divider"></div>

  <div class="contact">
    <p class="contact__name">EMPLOYEE NAME</p>
    <p class="contact__role">Director</p>
    <address class="contact__address">0000 your address Avenue<br>Cedar Hollow, ST 0000</address>
    <p class="contact__line">
      <svg class="contact__icon" viewBox="0 0 24 24" aria-label="Phone"><rect width="24" height="24" rx="4" fill="#f2f4f6"/><path d="M7 6h3l1 3-2 1.5a9 9 0 0 0 4.5 4.5L15 13l3 1v3a1 1 0 0 1-1 1A12 12 0 0 1 6 7a1 1 0 0 1 1-1z" fill="#1f2327"/></svg>
      000-000-0000
    </p>
    <p class="contact__line">
      <svg class="contact__icon" viewBox="0 0 24 24" aria-label="Fax"><rect width="24" height="24" rx="4" fill="#f2f4f6"/><rect x="7" y="5" width="10" height="5" fill="#1f2327"/><rect x="5" y="11" width="14" height="6" fill="#1f2327"/><rect x="7" y="15" width="10" height="4" fill="#1f2327"/></svg>
      000-000-0000
    </p>
    <p class="contact__line">
      <svg class="contact__icon" viewBox="0 0 24 24" aria-label="Email"><rect width="24" height="24" rx="4" fill="#f2f4f6"/><rect x="5" y="7" width="14" height="10" fill="none" stroke="#1f2327" stroke-width="1.6"/><polyline points="5,7 12,13 19,7" fill="none" stroke="#1f2327" stroke-width="1.6"/></svg>
      your@yourmail.com
    </p>
    <p class="contact__web">www.yourwebsite.com</p>
  </div>
</section>

</body>
</html>
```